App for Lawyers & Accountants needs 'Professional' Styling

We want to style our app to convey a 'Professional' appearance. It's used by Lawyers, Accountants, Doctors etc. who take their work very seriously.

We currently trying to follow corvane layout guidelines, but we find our app looks very bland. I've uploaded a screenshot of our current app, and two mock-ups of more stylized versions, but we're not happy with those mock-ups.

We'd like to see alternate designs for those two mock-ups, that look much more professional.

The specific elements we'd like to improve/focus on are:
* Colour of the top and left nav bars
* Appearance of the left nav, size, icons spacing
* Appearance of the buttons on the top right, so the user knows they are buttons they can press
* Spacing of the dashboard, background colour and spacing, colour/layout of the 'overdue' and 'todo' accordion headings in the 'my tasks' section.
* List view background grey, to be consistent with dashboard, but unobtrusive
* List view tabs to be obvious as tabs, but 'saved searches', filters and the export icon to still be associated with the data displayed, but it should be obvious to the user that those are different buttons, not just more tabs. (I.e. the filters button opens a panel below it that allows the user to filter the data in the list.)
* General appearance of the popup menu when you push the 'add' button on the top right

However, despite those specifics I'm sure it's all the subtle elements of the design that make a big difference.

Our brand colour is 1D4F91, and we use A20067 as a secondary colour in print media, (although it doesn't seem to work to well within the app.) Our brand font is signika. We'd like the designs to be based on those colours & font.

Professional people, Lawyers, Accountants, Doctors etc.

Sans Serif
• Signika

0255a3

• The most 'Professional' experience/quality possible. Think the quality & brand image of brindlewave desk, but taken to a higher level.
• An example/mock-up of the dashboard, list view and 'add' item popup menu
• Display the dashboard cards with the same information as our mock-ups - the information there is important and we don't have any extra cards to add (in the near term)
• Various colour combinations for the top and left nav bars, based on our primary blue brand colour, and perhaps some shade of dark grey.

```html
<!DOCTYPE html>
<html lang="en">
<head>
<meta charset="utf-8">
<title>Velmora – Dashboard and Matters</title>
<link rel="stylesheet" href="https://fonts.googleapis.com/css2?family=Signika:wght@300;400;500;600&display=swap">
<style>
:root{
  --brand:#1d4f91;
  --brand-dark:#173f78;
  --brand-deep:#133666;
  --brand-line:#2a5a9b;
  --accent:#a20067;
  --orange:#ee5a24;
  --yellow:#f2c14e;
  --page:#ffffff;
  --canvas:#f3f4f6;
  --card:#ffffff;
  --border:#dfe3e8;
  --rule:#e8ebef;
  --ink:#2b2f36;
  --muted:#7b838e;
  --label:#3a3f47;
}
*{box-sizing:border-box;margin:0;padding:0}
html,body{width:998px;height:1200px;overflow:hidden;background:var(--page)}
body{font-family:"Signika",sans-serif;color:var(--ink);font-weight:400}
.stage{position:absolute;left:0;top:0;width:1246px;height:1500px;transform:scale(0.8);transform-origin:0 0}
.screen{position:absolute;left:20px;width:1206px;height:721px;background:var(--canvas);box-shadow:0 2px 10px rgba(20,40,70,.12);overflow:hidden}
.screen--dashboard{top:17px}
.screen--matters{top:756px}
.icon{width:18px;height:18px;fill:none;stroke:currentColor;stroke-width:1.6;stroke-linecap:round;stroke-linejoin:round;display:inline-block;vertical-align:middle}

/* side navigation */
.sidenav{position:absolute;left:0;top:0;width:76px;height:721px;background:linear-gradient(180deg,var(--brand) 0%,var(--brand-dark) 100%)}
.sidenav__logo{position:absolute;left:18px;top:13px;width:40px;height:40px;border-radius:50%;background:#3c5f92;color:#dfe7f3;font-size:9px;display:flex;align-items:center;justify-content:center;letter-spacing:.5px}
.sidenav__item{position:absolute;left:0;width:76px;height:62px;display:flex;align-items:center;justify-content:center;color:#a9bedb;border-top:1px solid var(--brand-line)}
.sidenav__item .icon{width:19px;height:19px}
.sidenav__item--active{background:#2461ad;color:#ffffff}

/* header */
.topbar{position:absolute;left:76px;top:0;right:0;height:66px;background:#fff;border-bottom:1px solid var(--border)}
.topbar__title{position:absolute;top:24px;font-size:17px;color:var(--ink);font-weight:400}
.search{position:absolute;left:494px;top:17px;width:255px;height:35px;border:1px solid #c9d0d9;display:flex;align-items:center;padding-left:10px;gap:8px;color:var(--muted);font-size:12px}
.search .icon{width:16px;height:16px;color:#4a5563}
.action{position:absolute;top:16px;width:36px;height:36px;border:1.5px solid var(--brand);color:var(--brand);display:flex;align-items:center;justify-content:center;background:#fff}
.action--add{left:756px}.action--history{left:798px}.action--alerts{left:840px}
.action--open{box-shadow:0 0 0 3px rgba(29,79,145,.12)}
.profile__photo{position:absolute;left:892px;top:0;width:66px;height:66px;background:linear-gradient(160deg,#b9a48f 0%,#8a6f58 55%,#d8d4ce 100%)}
.profile__welcome{position:absolute;left:958px;top:0;width:133px;height:66px;background:var(--brand);color:#fff;padding:19px 0 0 15px}
.profile__welcome small{display:block;font-size:10px;color:#cfdcee}
.profile__welcome strong{display:block;font-size:14px;font-weight:600;margin-top:1px}
.profile__welcome .icon{position:absolute;right:10px;top:25px;width:14px;height:14px;color:#fff}

/* cards */
.section-title{position:absolute;font-size:10.5px;font-weight:600;letter-spacing:1px;color:var(--label);display:flex;align-items:center;gap:5px}
.section-title .icon{width:13px;height:13px;color:var(--brand)}
.card{position:absolute;background:var(--card);border:1px solid var(--border)}
.acc-head{height:44px;display:flex;align-items:center;padding:0 12px;font-size:13px;font-weight:500;border-bottom:1px solid var(--border);position:relative}
.badge{display:inline-block;margin-left:8px;padding:0 5px;font-size:10px;line-height:14px;border:1px solid var(--orange);color:var(--orange);font-weight:400}
.badge--blue{border-color:var(--brand);color:var(--brand)}
.acc-head .icon{position:absolute;right:12px;top:15px;width:13px;height:13px;color:#555}
.task{height:55.5px;position:relative;padding:11px 12px 0;border-bottom:1px solid var(--rule)}
.task:last-of-type{border-bottom:1px solid var(--border)}
.task__title{font-size:12.5px;color:var(--brand)}
.task__meta{font-size:10px;color:var(--muted);margin-top:3px;display:flex;align-items:center;gap:4px}
.task__meta .icon{width:11px;height:11px;color:var(--accent)}
.task__date{position:absolute;right:11px;top:22px;font-size:10px;color:var(--brand)}

.stats{display:flex;height:61px;border-bottom:1px solid var(--border)}
.stat{flex:1;text-align:center;padding-top:12px;border-right:1px solid var(--border)}
.stat:last-child{border-right:0}
.stat small{display:block;font-size:9px;letter-spacing:1px;color:var(--muted)}
.stat b{display:block;font-size:17px;color:var(--brand);font-weight:400;margin-top:2px}
.chart{position:absolute;left:0;top:61px}
.chart text{font-family:"Signika",sans-serif;font-size:7.5px;fill:#333}

.doc{height:56px;position:relative;padding:12px 0 0 34px;border-bottom:1px solid var(--rule)}
.doc:last-child{border-bottom:0}
.doc__name{font-size:12.5px;color:var(--brand)}
.doc__time{font-size:10px;color:var(--muted);margin-top:2px}
.doc__type{position:absolute;left:13px;top:19px;width:12px;height:15px}
.doc__type--sheet{background:#3f9a4f}
.doc__type--pdf{background:var(--orange)}
.doc .icon{position:absolute;right:11px;top:20px;width:17px;height:17px;color:var(--brand)}

.note{height:70px;position:relative;padding:14px 12px 0 31px;border-bottom:1px solid var(--rule)}
.note:last-child{border-bottom:0}
.note .icon{position:absolute;left:11px;top:22px;width:12px;height:12px;color:var(--accent)}
.note__title{font-size:12.5px;line-height:14px;color:var(--brand)}
.note__time{font-size:10px;color:var(--muted);margin-top:5px}

.footer{position:absolute;right:38px;top:686px;font-size:9px;letter-spacing:.4px;color:#555}

/* matters list */
.crumbs{position:absolute;left:97px;top:95px;font-size:12.5px;color:var(--ink);display:flex;align-items:center;gap:6px}
.crumbs a{color:var(--brand);text-decoration:none}
.crumbs .icon{width:11px;height:11px;color:#555}
.list-tool{position:absolute;top:94px;font-size:12.5px;color:var(--brand);display:flex;align-items:center;gap:5px}
.list-tool .icon{width:14px;height:14px}
.list-tool--filters{left:1012px}.list-tool--export{left:1115px}
.list{position:absolute;left:96px;top:136px;width:1071px;height:491px;background:#fff;border:1px solid var(--border)}
.tabs{height:54px;border-bottom:1px solid var(--border);display:flex;padding-left:19px}
.tab{font-size:10.5px;letter-spacing:1.2px;color:#5c636d;padding-top:22px;margin-right:53px;position:relative}
.tab--active{color:var(--ink);font-weight:600}
.tab--active::after{content:"";position:absolute;left:0;right:0;bottom:-1px;height:3px;background:var(--brand)}
.table{position:absolute;left:22px;top:92px;width:1048px;border-collapse:collapse}
.table th{font-size:10px;letter-spacing:1px;font-weight:600;color:var(--label);text-align:left;height:26px;vertical-align:top}
.table td{height:59.5px;font-size:12.5px;border-bottom:1px solid var(--rule)}
.table td.link{color:var(--brand)}
.pager{position:absolute;left:817px;top:441px;display:flex;align-items:center;font-size:11px;color:var(--ink)}
.pager__size{color:var(--brand);margin-right:8px;display:flex;align-items:center;gap:2px}
.pager__size .icon{width:9px;height:9px}
.page{width:20px;height:20px;border:1px solid #cfd4db;margin-left:6px;display:flex;align-items:center;justify-content:center;font-size:10px;color:#888}
.pager .page:first-of-type{margin-left:27px}
.page--current{border-color:var(--brand);color:var(--brand)}

.add-menu{position:absolute;left:699px;top:62px;width:298px;height:155px;background:#fff;box-shadow:0 4px 16px rgba(20,40,70,.18);display:grid;grid-template-columns:1fr 1fr;grid-template-rows:repeat(3,1fr)}
.add-menu::before{content:"";position:absolute;left:144px;top:-6px;width:12px;height:12px;background:#fff;transform:rotate(45deg)}
.add-menu__item{display:flex;align-items:center;justify-content:center;gap:5px;font-size:12.5px;color:var(--brand);border-bottom:1px solid var(--rule);border-right:1px solid var(--rule);position:relative}
.add-menu__item:nth-child(2n){border-right:0}
.add-menu__item:nth-last-child(-n+2){border-bottom:0}
.add-menu__item .icon{width:14px;height:14px;color:var(--accent)}
</style>
</head>
<body>
<svg width="0" height="0" style="position:absolute" aria-hidden="true">
  <defs>
    <symbol id="i-chart" viewBox="0 0 24 24"><path d="M4 20h16M5 20V10h4v10M10 20V5h4v15M15 20v-8h4v8"/></symbol>
    <symbol id="i-gavel" viewBox="0 0 24 24"><path d="M9 9l5-5 6 6-5 5zM11.5 11.5L3 20M12 21h9M7.5 7.5l9 9"/></symbol>
    <symbol id="i-user" viewBox="0 0 24 24"><circle cx="12" cy="8" r="4"/><path d="M4 21c1-5 4-7 8-7s7 2 8 7z"/></symbol>
    <symbol id="i-bell" viewBox="0 0 24 24"><path d="M6 17V11a6 6 0 0 1 12 0v6l2 2H4zM10 21h4"/></symbol>
    <symbol id="i-clip" viewBox="0 0 24 24"><path d="M20 11l-8 8a5 5 0 0 1-7-7l8-8a3.5 3.5 0 0 1 5 5l-8 8a2 2 0 0 1-3-3l7-7"/></symbol>
    <symbol id="i-history" viewBox="0 0 24 24"><path d="M4 12a8 8 0 1 0 2.5-5.8M4 4v4h4M12 8v4l3 2"/></symbol>
    <symbol id="i-gear" viewBox="0 0 24 24"><circle cx="12" cy="12" r="3"/><path d="M12 2l2 3 3.5-1 .5 3.5 3 2-2 3 2 3-3 2-.5 3.5-3.5-1-2 3-2-3-3.5 1-.5-3.5-3-2 2-3-2-3 3-2L6.5 4 10 5z"/></symbol>
    <symbol id="i-back" viewBox="0 0 24 24"><path d="M20 12H4M10 6l-6 6 6 6"/></symbol>
    <symbol id="i-search" viewBox="0 0 24 24"><circle cx="14" cy="10" r="6"/><path d="M9.5 14.5L4 20"/></symbol>
    <symbol id="i-plus" viewBox="0 0 24 24"><path d="M12 4v16M4 12h16"/></symbol>
    <symbol id="i-down" viewBox="0 0 24 24"><path d="M5 9l7 7 7-7"/></symbol>
    <symbol id="i-up" viewBox="0 0 24 24"><path d="M5 15l7-7 7 7"/></symbol>
    <symbol id="i-right" viewBox="0 0 24 24"><path d="M9 5l7 7-7 7"/></symbol>
    <symbol id="i-cloud" viewBox="0 0 24 24"><path d="M7 18a5 5 0 0 1 0-10 6 6 0 0 1 11 1.5A4.3 4.3 0 0 1 17.5 18M12 12v8M9 17l3 3 3-3"/></symbol>
    <symbol id="i-tag" viewBox="0 0 24 24"><path d="M3 12l9-9h8v8l-9 9zM16 7h.01"/></symbol>
    <symbol id="i-note" viewBox="0 0 24 24"><path d="M6 3h8l5 5v13H6zM14 3v5h5"/></symbol>
    <symbol id="i-filter" viewBox="0 0 24 24"><path d="M3 6h18M3 12h18M3 18h18M8 4v4M15 10v4M10 16v4"/></symbol>
    <symbol id="i-export" viewBox="0 0 24 24"><path d="M15 4H5v16h10M10 12h11M17 8l4 4-4 4"/></symbol>
  </defs>
</svg>

<div class="stage">

  <!-- Dashboard screen -->
  <section class="screen screen--dashboard">
    <nav class="sidenav">
      <div class="sidenav__logo">LOGO</div>
      <div class="sidenav__item sidenav__item--active" style="top:66px"><svg class="icon"><use href="#i-chart"/></svg></div>
      <div class="sidenav__item" style="top:128px"><svg class="icon"><use href="#i-gavel"/></svg></div>
      <div class="sidenav__item" style="top:190px"><svg class="icon"><use href="#i-user"/></svg></div>
      <div class="sidenav__item" style="top:253px"><svg class="icon"><use href="#i-bell"/></svg></div>
      <div class="sidenav__item" style="top:316px"><svg class="icon"><use href="#i-clip"/></svg></div>
      <div class="sidenav__item" style="top:378px;border-bottom:1px solid var(--brand-line)"><svg class="icon"><use href="#i-history"/></svg></div>
      <div class="sidenav__item" style="top:597px"><svg class="icon"><use href="#i-gear"/></svg></div>
      <div class="sidenav__item" style="top:659px"><svg class="icon"><use href="#i-back"/></svg></div>
    </nav>

    <header class="topbar">
      <h1 class="topbar__title" style="left:30px">Dashboard</h1>
      <div class="search"><svg class="icon"><use href="#i-search"/></svg>Search</div>
      <div class="action action--add"><svg class="icon"><use href="#i-plus"/></svg></div>
      <div class="action action--history"><svg class="icon"><use href="#i-history"/></svg></div>
      <div class="action action--alerts"><svg class="icon"><use href="#i-bell"/></svg></div>
      <div class="profile__photo" role="img" aria-label="Profile photo of the signed-in user"></div>
      <div class="profile__welcome"><small>Welcome</small><strong>Clara Voss</strong><svg class="icon"><use href="#i-down"/></svg></div>
    </header>

    <h2 class="section-title" style="left:107px;top:102px"><svg class="icon"><use href="#i-bell"/></svg>MY TASKS</h2>
    <div class="card" style="left:107px;top:124px;width:343px;height:258px">
      <div class="acc-head">Overdue <span class="badge">3</span><svg class="icon"><use href="#i-up"/></svg></div>
      <div class="task"><div class="task__title">Finalise Court Documents</div><div class="task__meta"><svg class="icon"><use href="#i-gavel"/></svg>1157 Ecerich v. The State of...</div><span class="task__date">23/05/18</span></div>
      <div class="task"><div class="task__title">Finalise Court Settlement Figures</div><div class="task__meta"><svg class="icon"><use href="#i-gavel"/></svg>P. Hegman</div><span class="task__date">23/05/18</span></div>
      <div class="task"><div class="task__title">Finalise Court Documents</div><div class="task__meta"><svg class="icon"><use href="#i-gavel"/></svg>1157 Ecerich v. The State of...</div><span class="task__date">23/05/18</span></div>
      <div class="acc-head" style="border-bottom:0">To Do <span class="badge badge--blue">51</span><svg class="icon"><use href="#i-down"/></svg></div>
    </div>

    <h2 class="section-title" style="left:466px;top:102px"><svg class="icon"><use href="#i-history"/></svg>MY TIME RECORDS</h2>
    <div class="card" style="left:466px;top:124px;width:344px;height:307px">
      <div class="stats">
        <div class="stat"><small>TODAY</small><b>5h</b></div>
        <div class="stat"><small>THIS WEEK</small><b>24h 7m</b></div>
        <div class="stat"><small>THIS WEEK</small><b>56h 34m</b></div>
      </div>
      <svg class="chart" width="342" height="244" viewBox="0 0 342 244" role="img" aria-label="Monthly hours bar chart">
        <g fill="#333">
          <text x="11" y="27">8H</text><text x="11" y="54">7H</text><text x="11" y="80">6H</text><text x="11" y="106">5H</text>
          <text x="11" y="132">4H</text><text x="11" y="158">3H</text><text x="11" y="184">2H</text><text x="11" y="210">1H</text>
        </g>
        <line x1="24" y1="14" x2="24" y2="218" stroke="#c9ced6"/>
        <g>
          <rect x="28" y="195" width="6" height="23" fill="var(--yellow)"/><rect x="34" y="183" width="6" height="35" fill="var(--orange)"/>
          <rect x="54" y="178" width="6" height="40" fill="var(--yellow)"/><rect x="60" y="162" width="6" height="56" fill="var(--orange)"/>
          <rect x="79" y="147" width="6" height="71" fill="var(--yellow)"/><rect x="85" y="120" width="6" height="98" fill="var(--orange)"/>
          <rect x="107" y="195" width="6" height="23" fill="var(--yellow)"/><rect x="113" y="186" width="6" height="32" fill="var(--orange)"/>
          <rect x="134" y="140" width="6" height="78" fill="var(--yellow)"/><rect x="140" y="110" width="6" height="108" fill="var(--orange)"/>
          <rect x="160" y="103" width="6" height="115" fill="var(--yellow)"/><rect x="166" y="58" width="6" height="160" fill="var(--orange)"/>
          <rect x="186" y="125" width="6" height="93" fill="var(--yellow)"/><rect x="192" y="89" width="6" height="129" fill="var(--orange)"/>
          <rect x="212" y="137" width="6" height="81" fill="var(--yellow)"/><rect x="218" y="106" width="6" height="112" fill="var(--orange)"/>
          <rect x="239" y="162" width="6" height="56" fill="var(--yellow)"/><rect x="245" y="140" width="6" height="78" fill="var(--orange)"/>
          <rect x="264" y="80" width="6" height="138" fill="var(--yellow)"/><rect x="270" y="26" width="6" height="192" fill="var(--orange)"/>
          <rect x="290" y="137" width="6" height="81" fill="var(--yellow)"/><rect x="296" y="105" width="6" height="113" fill="var(--orange)"/>
          <rect x="317" y="170" width="6" height="48" fill="var(--yellow)"/><rect x="323" y="152" width="6" height="66" fill="var(--orange)"/>
        </g>
        <g text-anchor="middle">
          <text x="34" y="229">JAN</text><text x="60" y="229">FEB</text><text x="85" y="229">MAR</text><text x="113" y="229">APR</text>
          <text x="140" y="229">MAY</text><text x="166" y="229">JUN</text><text x="192" y="229">JUL</text><text x="218" y="229">AUG</text>
          <text x="245" y="229">SEP</text><text x="270" y="229">OCT</text><text x="296" y="229">NOV</text><text x="323" y="229">DEC</text>
        </g>
      </svg>
    </div>

    <h2 class="section-title" style="left:466px;top:448px"><svg class="icon"><use href="#i-clip"/></svg>MY RECENT DOCUMENTS</h2>
    <div class="card" style="left:466px;top:470px;width:344px;height:114px">
      <div class="doc"><span class="doc__type doc__type--sheet"></span><div class="doc__name">Example Document.xl</div><div class="doc__time">1 Hour ago</div><svg class="icon"><use href="#i-cloud"/></svg></div>
      <div class="doc"><span class="doc__type doc__type--pdf"></span><div class="doc__name">Example Document.pdf</div><div class="doc__time">12/04/18</div><svg class="icon"><use href="#i-cloud"/></svg></div>
    </div>

    <h2 class="section-title" style="left:825px;top:102px"><svg class="icon"><use href="#i-bell"/></svg>MY TASKS</h2>
    <div class="card" style="left:825px;top:124px;width:343px;height:285px">
      <div class="note"><svg class="icon"><use href="#i-gavel"/></svg><div class="note__title">1157 Abobtt vs Director of Public Presecutions concerning &nbsp;motor vehicle</div><div class="note__time">7 Hours ago</div></div>
      <div class="note"><svg class="icon"><use href="#i-gavel"/></svg><div class="note__title">1157 Abobtt vs Director of Public Presecutions concerning &nbsp;motor vehicle</div><div class="note__time">23 Hours ago</div></div>
      <div class="note"><svg class="icon"><use href="#i-gavel"/></svg><div class="note__title">1157 Abobtt vs Director of Public Presecutions concerning &nbsp;motor vehicle</div><div class="note__time">3 Days ago</div></div>
      <div class="note"><svg class="icon"><use href="#i-gavel"/></svg><div class="note__title">1157 Abobtt vs Director of Public Presecutions concerning &nbsp;motor vehicle</div><div class="note__time">1 Month ago</div></div>
    </div>

    <p class="footer">VELMORA © 2018</p>
  </section>

  <!-- Matters screen -->
  <section class="screen screen--matters">
    <nav class="sidenav">
      <div class="sidenav__logo">LOGO</div>
      <div class="sidenav__item" style="top:66px"><svg class="icon"><use href="#i-chart"/></svg></div>
      <div class="sidenav__item sidenav__item--active" style="top:128px"><svg class="icon"><use href="#i-gavel"/></svg></div>
      <div class="sidenav__item" style="top:190px"><svg class="icon"><use href="#i-user"/></svg></div>
      <div class="sidenav__item" style="top:253px"><svg class="icon"><use href="#i-bell"/></svg></div>
      <div class="sidenav__item" style="top:316px"><svg class="icon"><use href="#i-clip"/></svg></div>
      <div class="sidenav__item" style="top:378px;border-bottom:1px solid var(--brand-line)"><svg class="icon"><use href="#i-history"/></svg></div>
      <div class="sidenav__item" style="top:597px"><svg class="icon"><use href="#i-gear"/></svg></div>
      <div class="sidenav__item" style="top:659px"><svg class="icon"><use href="#i-back"/></svg></div>
    </nav>

    <header class="topbar">
      <h1 class="topbar__title" style="left:20px">Matters</h1>
      <div class="search"><svg class="icon"><use href="#i-search"/></svg>Search</div>
      <div class="action action--add action--open"><svg class="icon"><use href="#i-plus"/></svg></div>
      <div class="action action--history"><svg class="icon"><use href="#i-history"/></svg></div>
      <div class="action action--alerts"><svg class="icon"><use href="#i-bell"/></svg></div>
      <div class="profile__photo" role="img" aria-label="Profile photo of the signed-in user"></div>
      <div class="profile__welcome"><small>Welcome</small><strong>Clara Voss</strong><svg class="icon"><use href="#i-down"/></svg></div>
    </header>

    <div class="crumbs"><a href="#">Matters</a><svg class="icon"><use href="#i-right"/></svg><span>My Matters</span></div>
    <div class="list-tool list-tool--filters"><svg class="icon"><use href="#i-filter"/></svg>Filters<svg class="icon" style="width:10px;height:10px"><use href="#i-down"/></svg></div>
    <div class="list-tool list-tool--export"><svg class="icon"><use href="#i-export"/></svg>Export</div>

    <div class="list">
      <div class="tabs">
        <span class="tab tab--active">MY MATTERS</span>
        <span class="tab">RECENT MATTERS</span>
        <span class="tab">ALL MATTERS</span>
      </div>
      <table class="table">
        <colgroup><col style="width:461px"><col style="width:145px"><col style="width:172px"><col style="width:135px"><col></colgroup>
        <thead><tr><th>TITLE</th><th>CLIENT</th><th>PRACTICE AREA</th><th>STATUS</th><th>LAST UPDATED</th></tr></thead>
        <tbody>
          <tr><td class="link">Abbott v. Moore concerning sale #707</td><td class="link">M Hamill</td><td>Conveyancing</td><td>Sign up</td><td>30/06/2017</td></tr>
          <tr><td class="link">Abernathy v. Director of Public Prosecutions con deceased #310</td><td class="link">Nicholas Inc.</td><td>Estates</td><td>Settlement</td><td>16/04/2017</td></tr>
          <tr><td class="link">Abernathy v. Director of Public Prosecutions con investment #578</td><td class="link">Little &amp; Rogan</td><td>Property</td><td>Settlement</td><td>05/03/2017</td></tr>
          <tr><td class="link">Abernathy v. Director of Public Prosecutions con work cover #295</td><td class="link">D’Amore Zieman</td><td>Personal Injury</td><td>Sign up</td><td>02/09/2017</td></tr>
          <tr><td class="link">Abernathy v. Schmitt concerning retail lease #668</td><td class="link">Witting &amp; Leucscke</td><td>Property</td><td>Settlement</td><td>15/11/2017</td></tr>
        </tbody>
      </table>
      <div class="pager">
        <span class="pager__size">20<svg class="icon"><use href="#i-down"/></svg></span>per page
        <span class="page page--current">1</span><span class="page">2</span><span class="page">3</span><span class="page">4</span><span class="page">5</span>
      </div>
    </div>

    <div class="add-menu">
      <div class="add-menu__item"><svg class="icon"><use href="#i-history"/></svg>Time</div>
      <div class="add-menu__item"><svg class="icon"><use href="#i-clip"/></svg>Document</div>
      <div class="add-menu__item"><svg class="icon"><use href="#i-tag"/></svg>Task</div>
      <div class="add-menu__item"><svg class="icon"><use href="#i-note"/></svg>Notes</div>
      <div class="add-menu__item"><svg class="icon"><use href="#i-gavel"/></svg>Matter</div>
      <div class="add-menu__item"><svg class="icon"><use href="#i-user"/></svg>Contact</div>
    </div>

    <p class="footer">VELMORA © 2018</p>
  </section>

</div>
</body>
</html>
```